Office brochure for chronic pain doctor

I need an brochure for my office, and since I want to be able to mail the brochure, I think trifold would be the best size. I treat patients with chronic head and neck pain, as well as sleep apnea. I treat all of the following:

1. headaches
2. myofascial pain, which is a fancy way of saying muscle pain
3. neuropathic pain, which is a fancy way of saying nerve pain
4. TMJ, which stands for the temporomandibular joint (jaw joint)
5. obstructive sleep apnea

The colors will be based on my logo on my website, which you can see at www.BrightJPR.net, and you can learn more about what I do at my website. JPR stands for orofacial pain, which is a speciality training within the field of dentistry but I do not treat teeth. I have high resolution graphics for the brochure so I need someone with an artistic eye to design and lay out the brochure.

The logo colors are:
Purple 9e80bb
Pink f6b1d0
Blue 0f4b8f
Updates

I had a request for the logo in a .ai or .pdf format, which I have just uploaded. Please let me know if you have any other requests. Thank you, Dale

Target Market(s)

80% female, 20% male. I am in an upscale area of Los Angeles called Beverly Hills but I will see a patient from any area around Los Angeles or from any area in the world.

Industry/Entity Type

Training

Colors
6b449b
e567a6
0355a3

Requirements
Must have
• I want a small section of the brochure to feature each of the five areas I treat, and I have included an image to place in each of the five sections. A small section should include a short bio of me, which you can condense from www.brightjpr.net/dale. The brochure must appeal to women since 80% of my patients are female but I don't want to completely ignore men. Most of the pain patients are female, and most of the sleep apnea patients are male.

Here are the colors in my logo
Purple 9e80bb
Pink f6b1d0
Blue 0f4b8f
Should not have
• Anything related to teeth or dentistry.
No decorative or script fonts.

```html
<!DOCTYPE html>
<html lang="en">
<head>
<meta charset="utf-8">
<title>Trifold Brochure – Caring for Head Pain and Sleep Apnea</title>
<link href="https://fonts.googleapis.com/css2?family=Didact+Gothic&family=Questrial&family=PT+Sans&display=swap" rel="stylesheet">
<style>
  :root {
    --navy: #0d3560;
    --ink: #123f70;
    --brand-blue: #0f4b8f;
    --brand-pink: #f6b1d0;
    --brand-purple: #9e80bb;
    --grad-top: #2b5283;
    --grad-mid: #a795b0;
    --grad-pink: #f0bdbd;
    --paper: #ffffff;
    --label: #9a9a9a;
    --fold: #8a8a8a;
    --photo-a: #4e5a5c;
    --photo-b: #c9ccd3;
  }
  * { box-sizing: border-box; margin: 0; padding: 0; }
  html, body { width: 1200px; height: 1000px; overflow: hidden; background: var(--paper); }
  body { position: relative; font-family: "Didact Gothic", "Century Gothic", sans-serif; color: var(--ink); }

  .panel-label {
    position: absolute; top: 152px; width: 200px; text-align: center;
    font-family: "PT Sans", sans-serif; font-size: 11px; color: var(--label);
  }

  .sheet {
    position: absolute; left: 204px; top: 195px; width: 793px; height: 613px;
    border: 1px solid #c8c8c8;
    background: linear-gradient(180deg, var(--grad-top) 0%, var(--grad-mid) 13%, var(--grad-pink) 36%, #f7dcda 52%, var(--paper) 65%);
    overflow: hidden;
  }
  .fold { position: absolute; top: 0; bottom: 0; border-left: 1px dashed var(--fold); }

  /* inside flap */
  .bio-name { position: absolute; left: 14px; top: 32px; font-size: 19px; color: var(--paper); font-weight: 400; }
  .bio-body { position: absolute; left: 14px; top: 60px; width: 232px; font-size: 10.6px; line-height: 15.1px; text-align: justify; hyphens: auto; }
  .bio-body p + p { margin-top: 15px; }
  .portrait {
    float: left; width: 117px; height: 126px; margin: 0 6px 2px 0;
    background: linear-gradient(160deg, var(--photo-a) 0%, #6b7577 45%, var(--photo-b) 100%);
  }
  .testimonials { position: absolute; left: 14px; top: 482px; width: 232px; }
  .testimonials h3 { font-size: 12px; font-weight: 400; color: var(--navy); margin-bottom: 7px; }
  .testimonials p { font-size: 10.6px; line-height: 15px; font-style: italic; }

  /* back cover */
  .callout {
    position: absolute; left: 277px; top: 73px; width: 232px; height: 242px;
    border: 1px solid var(--paper); text-align: center; padding-top: 16px;
    font-size: 16px; line-height: 22px;
  }
  .callout p { margin-bottom: 20px; }
  .callout .light { color: var(--paper); }
  .callout .dark { color: var(--navy); }
  .contact {
    position: absolute; left: 262px; top: 484px; width: 262px; text-align: center;
    font-family: "PT Sans", sans-serif; font-size: 12px; line-height: 16.8px; color: var(--brand-blue);
  }
  .contact .phone { margin-top: 16px; }

  /* front cover */
  .cover-title {
    position: absolute; left: 542px; top: 68px; font-family: "Questrial", sans-serif;
    font-size: 40px; line-height: 54.3px; font-weight: 400; color: var(--navy); letter-spacing: -0.3px;
  }
  .brand { position: absolute; left: 542px; top: 485px; width: 236px; height: 74px; display: flex; align-items: center; gap: 12px; }
  .brand-square { width: 74px; height: 74px; border-radius: 2px; background: var(--brand-purple); }
  .brand-name { font-family: "Questrial", sans-serif; font-size: 30px; color: var(--brand-blue); }
</style>
</head>
<body>
  <div class="panel-label" style="left:213px">Inside` Flap</div>
  <div class="panel-label" style="left:495px">Back Cover</div>
  <div class="panel-label" style="left:750px">Front Cover</div>

  <section class="sheet">
    <div class="fold" style="left:261px"></div>
    <div class="fold" style="left:526px"></div>

    <!-- inside flap -->
    <h2 class="bio-name">Oliamiammii Riiichjskl</h2>
    <div class="bio-body">
      <p><span class="portrait" role="img" aria-label="Portrait photo of the doctor in a white coat"></span>Delestrud delit velenia nbj utatumsan laoreet, consequipit am, se feu faccum ea con ut wisdigna faccumbj hhghdeliquis nostrud tionum trud tin ut praestisl ulla facidui bla consed dolum inisl ulput iuscipit velessim essecte elesequissim doloreet ut nonummod te commodo lestrud magnim eugue feuguer sim ad et lut ero con erostrud magna facin henit nostinim quatue dio cor si.</p>
      <p>Em dit lum zzrit lam velendignisi blaortie commodo lobortissi te feumsan vullan ut vulla facip et utpat. Duisl iriusciduisi bla feu facidunt utpat wisim ad del et wissis nibh eriuscidunt landre del ulla adip eu faccum ad modolore etum aciniamet, quatuer augiatue.</p>
      <p>Em dit lum zzrit lam velendignisi blaortie commodo lobortissi te feumsan vullan ut vulla facip et utpat. Duisl iriusciduisi</p>
    </div>
    <div class="testimonials">
      <h3>TESTIMONIALS</h3>
      <p>Ed eum verat lor in hent adigna coreros dolorpero odigna adiatie vel dolorer se magna faccum vel inismod olorem velenibh enis eugait ipismodolut ipismod oluptat. Ut inibh</p>
    </div>

    <!-- back cover -->
    <div class="callout">
      <p class="light">Henducient. Do, Catuus-<br>simens et abus iam sus</p>
      <p class="light">terferb itilincum ina, se<br>efachuit; nocto</p>
      <p class="dark">Henducient. Do, Catuus-<br>simens et abus iam sus<br>pub</p>
    </div>
    <address class="contact" style="font-style:normal">
      Dale Merriwether, DDS, MBA<br>
      Diplomate National Board of Facial Pain Care<br>
      4120 Larchmont Avenue, Suite 210<br>
      Beverly Hills, CA 90211
      <div class="phone">888.555.0142</div>
    </address>

    <!-- front cover -->
    <h1 class="cover-title">CARING<br>FOR<br>HEAD PAIN<br>AND<br>SLEEP APNEA</h1>
    <div class="brand">
      <span class="brand-square"></span>
      <span class="brand-name">BrightJPR</span>
    </div>
  </section>
</body>
</html>
```